Naturkosmetikpraxis sucht Design
Der Designer konnte gut meine Vorstellungen umsetzen und das in kürzester Zeit. Eine super Leistung, vor allem da ich weiß, dass es mir oft schwerfällt, mich klar auszudrücken.
Zielgruppe
Kosmetikpraxis, alle Altersgruppen aber Fokus Best Ager, vorwiegend weiblich, naturverbundene Menschen, gesundheitsbewusste Menschen, gestresste
gefallen soll es Menschen mit Hautproblemen und welchen, die einfach entspannen möchten.
Menschen, die Individualität suchen - nicht preiswerte Masse.
Aufgabenstellung
natürliche Hautpflegekonzepte,
Sugaring-Enthaarung, Wellness-Massagen, Naturnagelpflege, Wimpernlifting, Micro-Needling mit Lifting Pen, Klangschalenmassage, Permanent MakeUp
- Text mit Öffnungszeiten im Anhang "Banner..."
Als Farbe mag ich sehr dunkles rot, geht aber auch als Hintergrundfarbe. Ist wohl Brombeer etwa r171, g22, b78. Es geht ja hier um einen Banner für das Hoftor als Holz an einem Fachwerkhaus.
Habe noch ein paar Fotos aus meinem Bestand beigefügt.
Anderes Bild natürlich auch o.k.
BILD: 48193527 Frau m. Freesie von Bildarix. Das anhängende Bild flieder bluete 71846302 geht in eine ganz andere Richtung, ich weiß. Aber es ist ein tolles Bild und ich wäre durchaus bereit, auf flieder im Design zu wechseln. 08.04.14: jetzt hat sich das LOGO doch verändert.

```html
<!DOCTYPE html>
<html lang="de">
<head>
<meta charset="utf-8">
<title>Jana Lindholm Kosmetikpraxis</title>
<link href="https://fonts.googleapis.com/css2?family=Arimo:wght@400;700&display=swap" rel="stylesheet">
<style>
:root{
  --berry:#a3174f;
  --berry-dark:#6e0f33;
  --white:#ffffff;
  --grey-text:#4a4a4a;
  --silver-a:#f2f2f2;
  --silver-b:#bdbdbd;
}
*{margin:0;padding:0;box-sizing:border-box}
html,body{width:1200px;height:2519px;overflow:hidden;background:var(--white)}
body{font-family:"Arimo",Arial,sans-serif;position:relative}
.banner{position:relative;width:1200px;height:2519px;overflow:hidden;background:var(--white)}
.portrait{position:absolute;left:0;top:380px;width:1200px;height:1560px;
  background:
    radial-gradient(ellipse 620px 800px at 640px 700px,#e9c9b3 0%,#d7ab90 40%,rgba(215,171,144,0) 75%),
    linear-gradient(100deg,#6b4632 0%,#8a5d42 30%,#c9a38a 55%,#f4efec 78%,#ffffff 100%);}
.shapes{position:absolute;left:0;top:0}
.logo-tile{position:absolute;right:0;top:0;width:423px;height:177px;
  background:linear-gradient(135deg,var(--silver-a),var(--silver-b));
  display:flex;align-items:center;justify-content:center;gap:18px}
.logo-tile .dot{width:34px;height:34px;border-radius:50%;background:var(--berry)}
.logo-tile .name{font-size:64px;color:var(--berry);font-weight:400}
.owner{position:absolute;top:180px;left:50px;width:1200px;text-align:center;color:var(--white);font-size:116px;font-weight:400;letter-spacing:-1px}
.practice{position:absolute;top:305px;left:0;width:1200px;text-align:center;color:var(--white);font-size:74px}
.services{position:absolute;left:592px;top:1270px;list-style:none}
.services li{font-size:47px;line-height:66px;color:var(--berry);display:flex;align-items:center}
.services li::before{content:"";width:26px;height:26px;border-radius:50%;background:var(--berry);margin-right:22px;flex:none}
.web{font-family:"Arimo",Arial,sans-serif;font-size:56px;fill:var(--white)}
.phone{position:absolute;left:0;width:1200px;top:2028px;text-align:center;font-size:104px;font-weight:700;color:var(--berry)}
.mail{position:absolute;left:0;width:1200px;top:2150px;text-align:center;font-size:41px;color:var(--berry)}
.hours{position:absolute;left:0;top:2230px;width:1200px;height:289px;
  background:linear-gradient(90deg,#9e9e9e,#e6e6e6 35%,#f3f3f3 50%,#e6e6e6 65%,#9e9e9e);
  text-align:center;color:var(--grey-text);padding-top:22px}
.hours h2{font-size:50px;font-weight:700;margin-bottom:6px}
.hours p{font-size:40px;line-height:54px}
</style>
</head>
<body>
<div class="banner">
  <div class="portrait" role="img" aria-label="Porträtfoto einer jungen Frau mit geflochtenem Zopf und natürlicher, gepflegter Haut"></div>

  <svg class="shapes" width="1200" height="2519" viewBox="0 0 1200 2519">
    <defs>
      <linearGradient id="topBand" x1="0" y1="0" x2="1" y2="0">
        <stop offset="0" stop-color="#b01a55"/>
        <stop offset="1" stop-color="#6e0f33"/>
      </linearGradient>
      <linearGradient id="lowBand" x1="0" y1="0" x2="1" y2="0">
        <stop offset="0" stop-color="#a3174f"/>
        <stop offset="1" stop-color="#5e0c2b"/>
      </linearGradient>
    </defs>
    <path d="M0 0 H1200 V560 Q760 440 0 470 Z" fill="url(#topBand)"/>
    <path d="M0 470 Q760 440 1200 560 V610 Q760 480 0 520 Z" fill="#ffffff" opacity="0.85"/>
    <path d="M0 500 Q760 470 1200 590" fill="none" stroke="#e7a8bf" stroke-width="6"/>
    <path d="M0 2010 Q600 1870 1200 1830 V2519 H0 Z" fill="#ffffff"/>
    <path d="M0 1820 Q600 1720 1200 1700 V1830 Q600 1870 0 2010 Z" fill="url(#lowBand)"/>
    <path d="M0 2028 Q600 1890 1200 1852" fill="none" stroke="#e8b4c6" stroke-width="9"/>
    <path d="M420 2040 Q800 1920 1200 1885" fill="none" stroke="#f1cdd9" stroke-width="5"/>
    <text class="web" x="160" y="1955" transform="rotate(-9.5 160 1955)">www.kosmetikstudio-lindholm.de</text>
  </svg>

  <div class="logo-tile"><span class="dot"></span><span class="name">Sanfthaut</span></div>

  <div class="owner">Jana Lindholm</div>
  <div class="practice">Kosmetikpraxis</div>

  <ul class="services">
    <li>Natürliche Hautpflege</li>
    <li>Sugaring-Enthaarung</li>
    <li>Wellnessmassagen</li>
    <li>Maniküre</li>
    <li>Wimpernlifting</li>
    <li>Permanent Make-Up</li>
  </ul>

  <div class="phone">06123/ 457810</div>
  <div class="mail">info@naturkosmetik-auental.de</div>

  <section class="hours">
    <h2>Öffnungszeiten</h2>
    <p>Mo 15-19 Uhr nur Verkauf</p>
    <p>Di, Mi, Fr 09.30 - 13.00 Uhr und 14 - 18 Uhr</p>
    <p>Do 14 - 20 Uhr &nbsp;I&nbsp; Sa 10 - 13 Uhr</p>
  </section>
</div>
</body>
</html>
```